Business Card Design

My husband & I have a singing business so just need a card with my husband's photo on it and our current logo. I have attached the logo on the top of a page plus a photo of my husband & our theme colour we would like is a black background with red writing to match our logo. If you can please also put somewhere on the card "Entertainment for any occasion inc. Pubs, Clubs, Birthday Parties or Weddings". The photo is on the poster attached if you are able to copy it please.

Industry/Entity Type

Business

Contact Information for Business Card

Rocco & Jen Farley
Mobile: 0498 362 514
Email: janice.brook@mailnest.example

```html
<!DOCTYPE html>
<html lang="en">
<head>
<meta charset="utf-8">
<title>Velvet Echo Entertainment – Business Card</title>
<link href="https://fonts.googleapis.com/css2?family=EB+Garamond:wght@400&display=swap" rel="stylesheet">
<style>
  :root {
    --backdrop: #2a2a2c;
    --card-black: #000000;
    --brand-red: #e0242c;
    --frame-red: #d8262e;
    --photo-light: #f1ece6;
    --photo-mid: #b98a6e;
    --photo-dark: #1d1a1a;
  }
  html, body {
    margin: 0;
    padding: 0;
    width: 1200px;
    height: 900px;
    overflow: hidden;
    background: var(--backdrop);
  }
  .canvas {
    position: relative;
    width: 1200px;
    height: 900px;
  }
  .business-card {
    position: absolute;
    left: 100px;
    top: 145px;
    width: 1000px;
    height: 610px;
    background: var(--card-black);
    font-family: "EB Garamond", Georgia, serif;
    color: var(--brand-red);
    overflow: hidden;
  }
  .brand {
    position: absolute;
    left: 80px;
    top: 95px;
    width: 560px;
    display: flex;
    align-items: flex-start;
    gap: 18px;
  }
  .brand-mark {
    flex: 0 0 auto;
    width: 22px;
    height: 22px;
    margin-top: 24px;
    border-radius: 50%;
    background: var(--brand-red);
  }
  .brand-name {
    margin: 0;
    font-size: 60px;
    font-weight: 400;
    line-height: 1.05;
    color: var(--brand-red);
  }
  .brand-line {
    display: block;
    white-space: nowrap;
  }
  .brand-line--second {
    padding-left: 40px;
  }
  .tagline {
    position: absolute;
    left: 80px;
    top: 300px;
    width: 560px;
    margin: 0;
    font-size: 27px;
    line-height: 1.3;
  }
  .contact {
    position: absolute;
    left: 80px;
    top: 420px;
    width: 560px;
    margin: 0;
    font-size: 27px;
    line-height: 1.3;
    font-style: normal;
  }
  .contact p { margin: 0; white-space: nowrap; }
  .portrait {
    position: absolute;
    right: 52px;
    top: 40px;
    width: 240px;
    height: 526px;
    border: 3px solid var(--frame-red);
    background: linear-gradient(180deg, var(--photo-light) 0%, var(--photo-mid) 45%, var(--photo-dark) 80%);
  }
</style>
</head>
<body>
<main class="canvas">
  <section class="business-card">
    <div class="brand">
      <span class="brand-mark"></span>
      <h1 class="brand-name">
        <span class="brand-line">Velvet Echo</span>
        <span class="brand-line brand-line--second">Entertainment</span>
      </h1>
    </div>
    <p class="tagline">"Entertainment for any occasion inc.<br>Pubs, Clubs, Birthday Parties or Weddings"</p>
    <address class="contact">
      <p class="contact-names">Rocco &amp; Jen Farley</p>
      <p class="contact-phone">Mobile: 0498 362 514</p>
      <p class="contact-email">Email: janice.brook@mailnest.example</p>
    </address>
    <div class="portrait" role="img" aria-label="Portrait photo of the singer in a dark patterned shirt against a light background"></div>
  </section>
</main>
</body>
</html>
```